Visitenkarten-Design für Eventcatering & Gemeinschaftsverpflegung
Zielgruppe
Wir sind ein kreatives und aufstrebendes Unternehmen.
Seit jahren sind wir im Eventcatering und der Gemeinschaftsverpflegung tätig.
Als Marktführer kochen wir super leckeres Mittagessen für Grundschulen und Kindertagesstätten in Berlin und Brandenburg und bewirtschaften mehrere Betriebsrestaurants.
Wir sind sehr krativ und bleiben nie stehen, so bereichern wir die Gastronomie in allen
Bereichen mit immer neuen innovativen Ideen und der Leidenschaft zum gesunden und leckeren Essen.
We are a creative and ambitious company.
We have been active in event catering and community catering for years.
As the market leader, we cook delicious lunches for elementary schools and day-care centers in Berlin and Brandenburg and we run several company restaurants.
We are very creative and never stand still, this is how we enrich the gastronomy in all of them
areas with new, innovative ideas and a passion for healthy and delicious food.
Aufgabenstellung
Wir möchten gern die Rottöne aus unserem Logo wiederfinden.
Unser Logo darf im Vordergrund stehen.
We would like to find the red tones from our logo again.
Our logo can be in the foreground.

```html
<!DOCTYPE html>
<html lang="en">
<head>
<meta charset="utf-8">
<title>Kessa Catering – Business Card</title>
<link href="https://fonts.googleapis.com/css2?family=Open+Sans:wght@300;400;600&display=swap" rel="stylesheet">
<style>
  :root {
    --page-bg: #d9d9db;
    --card-white: #ffffff;
    --brand-red: #ee2224;
    --band-dark: #1c1c1c;
    --band-mid: #3a3a3a;
    --silver: #c4c4c4;
    --ink: #141414;
    --contact-text: #d6d6d6;
  }
  * { margin: 0; padding: 0; box-sizing: border-box; }
  html, body {
    width: 1200px; height: 977px; overflow: hidden;
    background: var(--page-bg);
    font-family: "Open Sans", Arial, sans-serif;
  }
  .canvas {
    width: 1200px; height: 977px;
    display: flex; flex-direction: column;
    align-items: center; justify-content: center; gap: 48px;
  }
  .card {
    position: relative;
    width: 760px; height: 434px;
    border-radius: 28px;
    overflow: hidden;
    box-shadow: 0 6px 18px rgba(0,0,0,.18);
  }
  .card--front { background: var(--card-white); }
  .card--back { background: var(--brand-red); display: flex; align-items: center; justify-content: center; }

  .brand {
    display: flex; align-items: center; gap: 18px;
  }
  .card--front .brand {
    position: absolute; top: 78px; left: 0; right: 0; justify-content: center;
  }
  .brand__mark { width: 54px; height: 54px; border-radius: 6px; }
  .card--front .brand__mark { background: var(--brand-red); }
  .card--back .brand__mark { background: var(--card-white); }
  .brand__name {
    font-size: 60px; font-weight: 600; color: var(--ink); letter-spacing: -1px;
  }

  .contact-band { position: absolute; inset: 0; }

  .contact-list {
    position: absolute; left: 0; right: 0; bottom: 34px;
    display: flex; justify-content: space-around; padding: 0 40px;
    list-style: none;
  }
  .contact-item {
    display: flex; flex-direction: column; align-items: center; gap: 10px;
    color: var(--contact-text); font-size: 16px; font-weight: 300; line-height: 1.35;
    text-align: center;
  }
  .contact-item__icon { width: 38px; height: 38px; }
</style>
</head>
<body>
<main class="canvas">

  <section class="card card--front" aria-label="Business card front">
    <svg class="contact-band" width="760" height="434" viewBox="0 0 760 434" aria-hidden="true">
      <defs>
        <linearGradient id="bandShade" x1="0" y1="0" x2="0" y2="1">
          <stop offset="0" stop-color="var(--band-mid)"/>
          <stop offset="1" stop-color="var(--band-dark)"/>
        </linearGradient>
      </defs>
      <path d="M0,262 Q380,182 760,262 L760,434 L0,434 Z" fill="url(#bandShade)"/>
      <path d="M0,262 Q380,182 760,262" fill="none" stroke="var(--silver)" stroke-width="6"/>
    </svg>

    <div class="brand">
      <span class="brand__mark"></span>
      <span class="brand__name">Kessa Catering</span>
    </div>

    <ul class="contact-list">
      <li class="contact-item">
        <svg class="contact-item__icon" viewBox="0 0 38 38" aria-hidden="true">
          <circle cx="19" cy="19" r="17" fill="none" stroke="var(--silver)" stroke-width="2"/>
          <path d="M13 11c1-1 2-1 3 0l2 3c.6 1 .3 1.8-.5 2.4l-1 .8c.8 2 2.4 3.6 4.4 4.4l.8-1c.6-.8 1.4-1.1 2.4-.5l3 2c1 1 1 2 0 3l-1.2 1.2c-1.5 1.5-5 .5-8.5-3s-4.5-7-3-8.5z" fill="var(--silver)"/>
        </svg>
        <span>700.555.0142<br>616.555.0187</span>
      </li>
      <li class="contact-item">
        <svg class="contact-item__icon" viewBox="0 0 38 38" aria-hidden="true">
          <circle cx="19" cy="19" r="17" fill="none" stroke="var(--silver)" stroke-width="2"/>
          <g fill="none" stroke="var(--silver)" stroke-width="1.6">
            <circle cx="19" cy="19" r="9"/>
            <ellipse cx="19" cy="19" rx="4" ry="9"/>
            <line x1="10" y1="19" x2="28" y2="19"/>
          </g>
        </svg>
        <span>tavelmark.com<br>ilva@tavelmark.com</span>
      </li>
      <li class="contact-item">
        <svg class="contact-item__icon" viewBox="0 0 38 38" aria-hidden="true">
          <circle cx="19" cy="19" r="17" fill="none" stroke="var(--silver)" stroke-width="2"/>
          <path d="M19 9a7 7 0 0 1 7 7c0 5-7 13-7 13s-7-8-7-13a7 7 0 0 1 7-7z" fill="var(--silver)"/>
          <circle cx="19" cy="16" r="2.6" fill="var(--band-dark)"/>
        </svg>
        <span>214 Harlow Lane<br>Ashby MI 48302</span>
      </li>
    </ul>
  </section>

  <section class="card card--back" aria-label="Business card back">
    <div class="brand">
      <span class="brand__mark"></span>
      <span class="brand__name">Kessa Catering</span>
    </div>
  </section>

</main>
</body>
</html>
```